Flyer-Design für Ergotherapie zu Hause
schönes Design, rasche Weiterentwicklung, ist auf meine Wünsche eingegangen, sehr netter und professioneller Kontakt. Vielen Dank für Ihre Arbeit. Alles gute Weiterhin.
Zielgruppe
Ergotherapie zu Hause.
Geriatrie, Neurologie und Handtherapie Klienten
Aufgabenstellung
Es wären auch 3 Flyer möglich mit ähnlichem Design jedoch mit den drei Fachrichtungen Geriatrie, Neurologie und Handtherapie Klienten.
2x3 Seitig gefalzt A4 Quer

```html
<!DOCTYPE html>
<html lang="de">
<head>
<meta charset="utf-8">
<title>Velthaus – Handtherapie bis Schulter</title>
<link href="https://fonts.googleapis.com/css2?family=Montserrat:wght@400;500;600;700&family=Lato:wght@400;700&display=swap" rel="stylesheet">
<style>
  :root{
    --page:#f3f1ed;
    --paper:#ffffff;
    --navy:#1c2540;
    --gold:#c99a3c;
    --sepia:#c3ae8c;
    --sepia-dark:#9c8462;
    --text:#6b6b6b;
    --rule:#e6e1d8;
  }
  *{box-sizing:border-box;margin:0;padding:0}
  html,body{width:1198px;height:1200px;overflow:hidden;background:var(--page)}
  body{font-family:"Lato",sans-serif;color:var(--text);position:relative}
  .brochure{position:absolute;left:39px;top:140px;display:flex;box-shadow:0 6px 24px rgba(0,0,0,.10)}
  .panel{position:relative;width:280px;height:594px;background:var(--paper);overflow:hidden;border-right:1px solid var(--rule)}
  .panel:last-child{border-right:none}
  .panel--cover{margin-left:0}
  .photo{position:absolute;border-radius:50%;background:radial-gradient(circle at 40% 40%,#d8c8ab,var(--sepia) 55%,var(--sepia-dark))}
  .dot{position:absolute;border-radius:50%}
  .dot--navy{background:var(--navy)}
  .dot--gold{background:var(--gold)}
  h2{font-family:"Montserrat",sans-serif;font-weight:600;color:var(--navy);font-size:19px;line-height:1.25}
  p,li{font-size:9.5px;line-height:1.6}
  .panel__body{position:absolute;left:28px;right:28px}
  .panel__body p+p{margin-top:8px}
  .contact{margin-top:16px}
  .contact p{margin:0}
  .goals{list-style:none;margin-top:12px}
  .goals li{position:relative;padding-left:14px;margin-bottom:9px}
  .goals li::before{content:"";position:absolute;left:0;top:5px;width:5px;height:5px;border-radius:50%;background:var(--gold)}
  .cover__title{font-size:22px;text-align:center}
  .cover__sub{text-align:center;margin-top:10px;font-size:9px}
  .brand{display:flex;flex-direction:column;align-items:center;gap:3px}
  .brand__name{font-family:"Montserrat",sans-serif;font-weight:600;letter-spacing:.28em;color:var(--navy);font-size:16px;display:flex;align-items:center;gap:8px}
  .brand__mark{width:8px;height:8px;border-radius:50%;background:var(--gold)}
  .brand__tag{font-family:"Montserrat",sans-serif;font-weight:600;letter-spacing:.18em;font-size:7px;color:var(--navy)}
  .page-brand{position:absolute;left:0;right:0;top:1010px}
  .page-brand .brand__name{font-size:20px}
  .page-brand .brand__tag{font-size:8.5px}
</style>
</head>
<body>
  <main class="brochure">
    <section class="panel panel--why">
      <div class="photo" style="left:-40px;top:-60px;width:300px;height:300px" role="img" aria-label="Foto: Hand beim Schreibtraining mit Stift auf Papier"></div>
      <div class="dot dot--navy" style="left:210px;top:218px;width:44px;height:44px"></div>
      <div class="dot dot--gold" style="left:150px;top:260px;width:14px;height:14px"></div>
      <div class="panel__body" style="top:300px">
        <h2>Warum Ergotherapie zu Hause?</h2>
        <div style="margin-top:16px">
          <p>Der Weg in eine Praxis ist oft mühsam. Viele Menschen sind in ihrer Mobilität eingeschränkt, daher komme ich zu Ihnen nach Hause.</p>
          <p>Die Ergotherapie im häuslichen Umfeld ermöglicht es, alltägliche Abläufe direkt dort zu üben, wo sie gebraucht werden. So lassen sich Hilfsmittel, Möbel und Wege gezielt anpassen.</p>
          <p>Das Ziel ist mehr Selbstständigkeit im Alltag und Sicherheit in den eigenen vier Wänden.</p>
        </div>
      </div>
    </section>

    <section class="panel panel--contact">
      <div class="panel__body" style="top:60px">
        <h2>Gerne beantworte ich Ihre Fragen</h2>
        <div class="contact">
          <p>Sie erreichen mich unter folgenden Kontaktdaten:</p>
        </div>
        <div class="contact">
          <p>Ergotherapie Morwitz</p>
          <p>Lindenweg 14</p>
          <p>76185 Karlsruhe</p>
        </div>
        <div class="contact">
          <p>talubo3@kreavoxo.de</p>
          <p>www.kreavoxo.de</p>
        </div>
        <div class="contact">
          <p>+49 721 555 0148</p>
        </div>
      </div>
      <div class="dot dot--gold" style="left:30px;top:330px;width:30px;height:30px"></div>
      <div class="photo" style="left:40px;top:350px;width:210px;height:210px" role="img" aria-label="Foto: Hände bei einer Greifübung"></div>
      <div class="dot dot--navy" style="left:210px;top:540px;width:30px;height:30px"></div>
    </section>

    <section class="panel panel--goals">
      <div class="panel__body" style="top:60px">
        <h2>Ziele der Ergotherapie</h2>
        <p style="margin-top:16px">Ziel der Therapie ist die Verbesserung der Handfunktion in Beruf und Alltag.</p>
        <ul class="goals">
          <li>Größere Beweglichkeit der Finger und Gelenke</li>
          <li>Kraft und Ausdauer der Hand aufbauen</li>
          <li>Narbenbehandlung nach Operationen</li>
          <li>Schmerzlinderung und Entlastung</li>
          <li>Sensibilitätstraining</li>
          <li>Anpassung von Schienen</li>
          <li>Hilfsmittelberatung für den Alltag</li>
        </ul>
      </div>
    </section>

    <section class="panel panel--cover">
      <div class="photo" style="left:60px;top:-40px;width:280px;height:280px" role="img" aria-label="Foto: Therapeutin behandelt eine Hand"></div>
      <div class="dot dot--navy" style="left:30px;top:170px;width:60px;height:60px"></div>
      <div class="dot dot--gold" style="left:240px;top:250px;width:14px;height:14px"></div>
      <div class="panel__body" style="top:330px">
        <h2 class="cover__title">Handtherapie bis Schulter</h2>
        <p class="cover__sub">Ergotherapie im Bereich Orthopädie</p>
      </div>
      <div class="brand" style="position:absolute;left:0;right:0;top:500px">
        <span class="brand__name"><span class="brand__mark"></span>VELTHAUS</span>
        <span class="brand__tag">ERGOTHERAPIE ZU HAUSE</span>
      </div>
    </section>
  </main>

  <footer class="brand page-brand">
    <span class="brand__name"><span class="brand__mark"></span>VELTHAUS</span>
    <span class="brand__tag">ERGOTHERAPIE ZU HAUSE</span>
  </footer>
</body>
</html>
```